Business Card Design Project

Business card design based on the existing logo.

Target Market(s)

Small to medium business owners and CIO's looking for professional IT services.

Industry/Entity Type

Business

Font styles to use
Serif
Sans Serif

Requirements
Must have
• Logo, company name, company details

Text to appear on the business card
Name / Title:
Leon Fairholt
CEO

Address:
Valtiro Limited
Level 3, 42 Kestle St
P O Box 462
Paraparaumu 5391

Other details:
leon@valtiro.co
Ph: 0800 519 308
Mob: +64 21 948 216
www.valtiro.co

Nice to have
• I would look at both single and double sided options. My initial thought is double sided with just the logo with the grey framing for the front and the name and details on the back. But I'm open to other design options.

```html
<!DOCTYPE html>
<html lang="en">
<head>
<meta charset="utf-8">
<title>Valtiro Business Card</title>
<link rel="stylesheet" href="https://fonts.googleapis.com/css2?family=Questrial&family=Mulish:wght@700&display=swap">
<style>
  :root {
    --backdrop: #d6d6d6;
    --card-white: #ffffff;
    --card-dark: #3a3a3a;
    --ink: #1c1c1c;
    --ink-soft: #333333;
    --brand-blue: #1a6a96;
    --mark-grey: #b9b9b9;
  }
  html, body {
    margin: 0;
    padding: 0;
    width: 1200px;
    height: 675px;
    overflow: hidden;
    background: var(--backdrop);
    font-family: "Questrial", "Century Gothic", sans-serif;
  }
  .stage {
    position: relative;
    width: 1200px;
    height: 675px;
  }
  .card {
    position: absolute;
    top: 188px;
    width: 520px;
    height: 298px;
    box-sizing: border-box;
    box-shadow: 0 6px 18px rgba(0,0,0,0.18);
  }
  .card-front {
    left: 50px;
    background: var(--card-white);
    color: var(--ink);
  }
  .card-back {
    left: 630px;
    background: var(--card-dark);
    color: var(--card-white);
  }
  .wordmark {
    position: absolute;
    display: flex;
    align-items: center;
    gap: 12px;
    line-height: 1;
  }
  .wordmark-dot {
    width: 30px;
    height: 30px;
    border-radius: 50%;
    background: var(--brand-blue);
  }
  .card-front .wordmark {
    left: 30px;
    top: 44px;
    font-size: 42px;
    color: var(--ink);
  }
  .card-back .wordmark {
    left: 50%;
    top: 50%;
    transform: translate(-50%, -50%);
    font-size: 58px;
    color: var(--card-white);
  }
  .card-back .wordmark-dot {
    width: 38px;
    height: 38px;
  }
  .contact-list {
    position: absolute;
    right: 26px;
    top: 40px;
    margin: 0;
    padding: 0;
    list-style: none;
    font-size: 12.5px;
    color: var(--ink-soft);
    text-align: right;
  }
  .contact-list li {
    display: flex;
    justify-content: flex-end;
    align-items: center;
    gap: 9px;
    height: 19px;
  }
  .contact-icon {
    width: 11px;
    height: 11px;
    fill: var(--brand-blue);
  }
  .person {
    position: absolute;
    left: 30px;
    top: 150px;
  }
  .person-name {
    margin: 0;
    font-family: "Mulish", "Century Gothic", sans-serif;
    font-weight: 700;
    font-size: 17px;
    color: var(--ink);
  }
  .person-title {
    margin: 1px 0 0;
    font-size: 15px;
    color: var(--brand-blue);
  }
  .address {
    position: absolute;
    left: 30px;
    bottom: 26px;
    margin: 0;
    font-style: normal;
    font-size: 12.5px;
    line-height: 19px;
    color: var(--ink-soft);
  }
</style>
</head>
<body>
<main class="stage">

  <section class="card card-front" aria-label="Business card front">
    <div class="wordmark">
      <span class="wordmark-dot"></span>
      <span class="wordmark-name">Valtiro</span>
    </div>

    <ul class="contact-list">
      <li>0800 519 308
        <svg class="contact-icon" viewBox="0 0 12 12" aria-hidden="true"><path d="M2.5 1h2l1 3-1.3 1a6 6 0 0 0 2.8 2.8l1-1.3 3 1v2a1.5 1.5 0 0 1-1.5 1.5A9.5 9.5 0 0 1 1 2.5 1.5 1.5 0 0 1 2.5 1z"/></svg>
      </li>
      <li>+64 21 948 216
        <svg class="contact-icon" viewBox="0 0 12 12" aria-hidden="true"><path d="M3.5 0h5a1 1 0 0 1 1 1v10a1 1 0 0 1-1 1h-5a1 1 0 0 1-1-1V1a1 1 0 0 1 1-1zm.5 1.5v7.5h4V1.5zM6 9.8a.7.7 0 1 0 0 1.4.7.7 0 0 0 0-1.4z"/></svg>
      </li>
      <li>leon@valtiro.co
        <svg class="contact-icon" viewBox="0 0 12 12" aria-hidden="true"><path d="M1 2.5h10v7H1zm.8.8v.4L6 6.6l4.2-2.9v-.4z"/></svg>
      </li>
      <li>www.valtiro.co
        <svg class="contact-icon" viewBox="0 0 12 12" aria-hidden="true"><circle cx="6" cy="6" r="5.3"/></svg>
      </li>
    </ul>

    <div class="person">
      <p class="person-name">Leon Fairholt</p>
      <p class="person-title">CEO</p>
    </div>

    <address class="address">
      Level 3, 42 Kestle St<br>
      P O Box 462<br>
      Paraparaumu 5391
    </address>
  </section>

  <section class="card card-back" aria-label="Business card back">
    <div class="wordmark">
      <span class="wordmark-dot"></span>
      <span class="wordmark-name">Valtiro</span>
    </div>
  </section>

</main>
</body>
</html>
```